New Webpage for High Class Expert Witness Services Company

We are looking for a minimalist design for a webpage that just has our logo and an entry form offer to connect with one of our Liaisons.
The entry form should just ask for Name, Email, Contact Info and Description of Project.

Company Name is: The Marlow Crest Advisory Services

Number of Pages Required

1 page

```html
<!DOCTYPE html>
<html lang="en">
<head>
<meta charset="UTF-8">
<title>Connect with a Liaison — The Marlow Crest Advisory Services</title>
<link href="https://fonts.googleapis.com/css2?family=Inter:wght@400;500;600;700&family=Newsreader:opsz,wght@6..72,400&display=swap" rel="stylesheet">
<style>
  :root{
    --page-bg:#141414;
    --card-bg:#121212;
    --card-border:#262626;
    --field-bg:#0f0f0f;
    --field-border:#3a3a3a;
    --text-strong:#f2f2f2;
    --text-body:#a8a8a8;
    --text-muted:#8a8a8a;
    --rule:#6a6a6a;
    --button-top:#f4f4f4;
    --button-bottom:#a9a9a9;
    --button-text:#111111;
  }
  *{box-sizing:border-box;margin:0;padding:0}
  html,body{width:1200px;height:750px;overflow:hidden}
  body{
    position:relative;
    background:var(--page-bg);
    font-family:"Inter",sans-serif;
    color:var(--text-strong);
  }
  .backdrop{
    position:absolute;inset:0;
    background:
      linear-gradient(180deg,#151515 0%,rgba(21,21,21,0.55) 20%,rgba(21,21,21,0.55) 80%,#1a1a1a 100%),
      linear-gradient(90deg,#2a2c2b 0%,#3a3d3b 18%,#2d2f2e 50%,#3b3f3d 82%,#2b2d2c 100%);
  }
  .brand{
    position:absolute;top:48px;left:0;width:100%;height:26px;
    display:flex;justify-content:center;align-items:center;gap:10px;
  }
  .brand-mark{width:14px;height:14px;background:#d8d8d8}
  .brand-name{
    font-family:"Inter",sans-serif;font-weight:500;font-size:17px;line-height:26px;
    letter-spacing:2.5px;text-transform:uppercase;color:#d8d8d8;
  }
  .card{
    position:absolute;left:201px;top:133px;width:798px;height:499px;
    background:var(--card-bg);border:1px solid var(--card-border);border-radius:6px;
  }
  .intro{position:absolute;left:26px;top:0;width:340px;height:100%;
    display:flex;flex-direction:column;justify-content:center}
  .intro-title{
    font-family:"Newsreader",serif;font-weight:400;font-size:42px;line-height:48px;
    color:var(--text-strong);
  }
  .intro-rule{width:40px;height:1px;background:var(--rule);margin:28px 0 22px}
  .intro-text{font-size:13.5px;line-height:20px;color:var(--text-body)}
  .liaison-form{position:absolute;left:426px;top:28px;width:347px}
  .field{margin-bottom:14px}
  .field-label{display:flex;align-items:center;gap:9px;font-size:12px;line-height:16px;font-weight:600;
    color:var(--text-strong);height:16px;margin-bottom:7px}
  .field-label svg{width:15px;height:15px;margin-left:2px;flex:none}
  .field-input{display:block;width:100%;height:37px;background:var(--field-bg);
    border:1px solid var(--field-border);border-radius:4px}
  .field-area{height:147px}
  .submit{
    display:block;width:100%;height:40px;border:none;border-radius:4px;
    background:linear-gradient(180deg,var(--button-top),var(--button-bottom));
    color:var(--button-text);font-family:"Inter",sans-serif;font-weight:700;font-size:13.5px;letter-spacing:.3px;
  }
  .footer{
    position:absolute;top:666px;left:0;width:100%;
    display:flex;justify-content:center;align-items:center;
    font-size:12px;color:var(--text-muted);
  }
  .footer span{padding:0 10px}
  .footer .sep{width:1px;height:18px;background:#555;padding:0}
</style>
</head>
<body>
  <div class="backdrop" role="img" aria-label="Dim photograph of a modern office interior with large windows"></div>

  <header class="brand">
    <span class="brand-mark"></span>
    <span class="brand-name">Marlow Crest Advisory Services</span>
  </header>

  <main class="card">
    <section class="intro">
      <h1 class="intro-title">Connect with a Liaison</h1>
      <div class="intro-rule"></div>
      <p class="intro-text">Connect with our experts to discuss your needs and discover how our platform can support your project.</p>
    </section>

    <form class="liaison-form">
      <div class="field">
        <label class="field-label">
          <svg viewBox="0 0 16 16" fill="none" stroke="#e0e0e0" stroke-width="1.2"><circle cx="8" cy="5" r="3"/><path d="M2.5 14.5c0-3 2.5-5 5.5-5s5.5 2 5.5 5z"/></svg>
          Name
        </label>
        <div class="field-input"></div>
      </div>
      <div class="field">
        <label class="field-label">
          <svg viewBox="0 0 16 16" fill="none" stroke="#e0e0e0" stroke-width="1.2"><rect x="1.5" y="3" width="13" height="10" rx="1.5"/><path d="M2 4l6 5 6-5"/></svg>
          Email
        </label>
        <div class="field-input"></div>
      </div>
      <div class="field">
        <label class="field-label">
          <svg viewBox="0 0 16 16" fill="none" stroke="#e0e0e0" stroke-width="1.2"><rect x="1.5" y="3" width="13" height="10" rx="1"/><rect x="3.5" y="5.5" width="3" height="3"/><path d="M8.5 6h4M8.5 8h4M3.5 10.5h9"/></svg>
          Contact Info
        </label>
        <div class="field-input"></div>
      </div>
      <div class="field">
        <label class="field-label">
          <svg viewBox="0 0 16 16" fill="none" stroke="#e0e0e0" stroke-width="1.2"><path d="M2 3.5h12M2 6.5h9M2 9.5h12M2 12.5h7"/></svg>
          Description of Project
        </label>
        <div class="field-input field-area"></div>
      </div>
      <button type="button" class="submit">SUBMIT</button>
    </form>
  </main>

  <footer class="footer">
    <span>Copyright © 2026 The Marlow Crest Advisory Services</span>
    <span class="sep"></span>
    <span>Privacy policy</span>
    <span class="sep"></span>
    <span>Terms and conditions</span>
  </footer>
</body>
</html>
```